Kveldbrá - Start-up company selling electricity

Hello let me tell you about Kveldbrá.

Kveldbrá is start-up company selling electricity in Iceland. The operations of the company consist of making power usage forecasts for our customers, purchasing the electricity wholesale from the energy producers, and selling the electricity to the consumer. We are focused on tech by using optimization and machine learning to minimize electricity prices to our customers. Our marketing strategy is to portray a tech company mindset and to show dedication to driving down the electricity price on the market.

We need your help to make our website pop. Possible concepts to work with are as follows:

- Iceland the land of ice and fire
- Green energy
- Innovation
- Tech and data science

Link to our website: https://prufa.kveldbra.is/
We are open to ideas.
Thank you!

Target Market(s)

Electricity consumers both homes and companies.

Number of Pages Required

1 page

Font styles to use
Serif
Sans Serif

```html
<!DOCTYPE html>
<html lang="is">
<head>
<meta charset="utf-8">
<title>Kveldbrá – Sama rafmagn, bara ódýrara</title>
<link href="https://fonts.googleapis.com/css2?family=Aldrich&family=Didact+Gothic&family=Cinzel:wght@500&display=swap" rel="stylesheet">
<style>
  :root{
    --orange:#f45a06;
    --green:#7f9f0a;
    --ink:#222;
    --heading:#5a5a5a;
    --card-edge:#9e9ea6;
    --footer:#333;
    --white:#fff;
  }
  *{box-sizing:border-box;margin:0;padding:0}
  html,body{width:1200px;height:991px;overflow:hidden;background:var(--white)}
  body{position:relative;font-family:"Didact Gothic",sans-serif;color:var(--ink)}

  .site-header{position:absolute;left:0;top:0;width:1200px;height:114px;background:var(--white);box-shadow:0 4px 14px rgba(0,0,0,.05);z-index:2}
  .brand{position:absolute;left:141px;top:34px;display:flex;align-items:center;gap:12px;font-family:"Aldrich",sans-serif;font-size:38px;color:var(--orange);letter-spacing:1px}
  .brand-dot{width:34px;height:34px;border-radius:50%;background:var(--orange)}
  .main-nav{position:absolute;top:47px;left:604px;font-family:"Aldrich",sans-serif;font-size:14px;color:#555}
  .main-nav a{color:inherit;text-decoration:none;position:absolute;white-space:nowrap}

  .backdrop{position:absolute;left:0;top:420px;width:1200px;height:338px;background:linear-gradient(180deg,rgba(235,235,235,0) 0%,rgba(232,232,232,.55) 45%,rgba(240,240,240,.3) 100%)}

  .hero-title{position:absolute;top:172px;left:0;width:1184px;text-align:center;font-family:"Aldrich",sans-serif;font-size:31px;font-weight:400;color:var(--heading);letter-spacing:.5px}

  .card{position:absolute;top:234px;width:295px;height:391px;background:var(--white);border:1px solid #ddd;border-bottom:4px solid var(--card-edge);text-align:center}
  .card-icon{position:absolute;left:50%;top:29px;width:122px;height:122px;margin-left:-61px;border:2px dotted #9a9a9a;border-radius:50%;display:flex;align-items:center;justify-content:center}
  .card-title{position:absolute;top:168px;left:0;width:100%;font-family:"Aldrich",sans-serif;font-size:14.5px;font-weight:400;color:var(--ink)}
  .card-text{position:absolute;top:201px;left:24px;right:24px;font-size:13.5px;line-height:19px}
  .card-text.narrow{left:44px;right:44px}
  .btn{position:absolute;top:324px;width:113px;height:39px;line-height:39px;text-align:center;color:var(--white);font-family:"Cinzel",serif;font-size:13px;letter-spacing:.8px;text-decoration:none}
  .btn-green{background:var(--green)}
  .btn-orange{background:var(--orange)}

  .price{position:absolute;top:204px;width:140px;text-align:center}
  .price-value{font-family:Arial,sans-serif;font-size:19px;display:block;margin-bottom:3px}
  .price-unit{font-size:13.5px;line-height:16px}
  .price-divider{position:absolute;left:144px;top:198px;width:1px;height:80px;background:#ddd}
  .compare-link{position:absolute;top:296px;left:0;width:100%;font-size:13.5px}

  .site-footer{position:absolute;left:0;top:758px;width:1200px;height:191px;background:var(--footer);color:var(--white)}
  .contact-icon{position:absolute;width:40px;height:39px;border:1px solid var(--orange);display:flex;align-items:center;justify-content:center}
  .contact-text{position:absolute;font-family:"Aldrich",sans-serif;font-size:14px;line-height:21px}
  .footer-brand{position:absolute;left:0;top:56px;width:1200px;font-family:"Aldrich",sans-serif;font-size:30px;color:var(--orange);display:flex;justify-content:center;align-items:center;gap:10px}
  .footer-brand .brand-dot{width:26px;height:26px}
  .company-info{position:absolute;top:138px;left:0;width:1200px;text-align:center;font-family:"Aldrich",sans-serif;font-size:12.5px;line-height:19px}
  .company-info .sep{margin:0 18px}
  .copyright{position:absolute;left:0;top:949px;width:1200px;height:42px;line-height:42px;background:var(--orange);color:var(--white);text-align:center;font-size:13px}
</style>
</head>
<body>

<header class="site-header">
  <div class="brand"><span class="brand-dot"></span>KVELDBRÁ</div>
  <nav class="main-nav">
    <a href="#" style="left:0">Viðskiptaskilmálar</a>
    <a href="#" style="left:180px">Spurt &amp; Svarað</a>
    <a href="#" style="left:328px;top:1px">Um Kveldbrá</a>
  </nav>
</header>

<div class="backdrop" role="img" aria-label="Faint line drawing of electricity pylons and power lines"></div>

<h1 class="hero-title">SAMA RAFMAGN - BARA ÓDÝRARA!</h1>

<section class="card" style="left:141px">
  <div class="card-icon">
    <svg width="46" height="62" viewBox="0 0 46 62" fill="none" stroke="var(--green)" stroke-width="2.5" stroke-linecap="round" stroke-linejoin="round">
      <path d="M14 2v12M32 2v12"/>
      <path d="M4 14h38v8"/>
      <path d="M8 22v8c0 10 7 16 15 16s15-6 15-16v-8"/>
      <path d="M4 22h38"/>
      <path d="M25 28l-5 6h6l-5 6"/>
      <path d="M23 46v6c0 5 4 8 10 8"/>
    </svg>
  </div>
  <h2 class="card-title">Velkomin Í Viðskipti</h2>
  <p class="card-text">Lorem ipsum dolor sit a consectetuer adipiscing elit, sed diam nonummy nibh euismod tincidunt ut laoreet dolore magna aliquam erat volutpat.Ut wisi enim ad minim veniam quis.</p>
  <a href="#" class="btn btn-green" style="left:26px">FYRIRTÆKI</a>
  <a href="#" class="btn btn-orange" style="left:146px">HEIMILI</a>
</section>

<section class="card" style="left:452px">
  <div class="card-icon">
    <svg width="52" height="64" viewBox="0 0 52 64" fill="none" stroke="var(--green)" stroke-width="2.5" stroke-linejoin="round">
      <path d="M2 2h40l8 8v52H2z"/>
      <path d="M42 2v8h8"/>
      <path d="M12 13h8M32 13h8M12 18h8M32 18h8"/>
      <text x="22" y="20" font-family="Arial,sans-serif" font-size="13" font-weight="700" fill="var(--green)" stroke="none">$</text>
      <rect x="10" y="28" width="7" height="6"/><path d="M22 29h20M22 33h20"/>
      <rect x="10" y="39" width="7" height="6"/><path d="M22 40h20M22 44h20"/>
      <rect x="10" y="50" width="7" height="6"/><path d="M22 51h20M22 55h20"/>
    </svg>
  </div>
  <h2 class="card-title">Verðskrá</h2>
  <div class="price" style="left:0"><span class="price-value">6.95</span><span class="price-unit">krónur / kWst</span></div>
  <div class="price-divider"></div>
  <div class="price" style="left:140px;width:155px"><span class="price-value">6.22</span><span class="price-unit">krónur / kWst<br>rafmagnskynding</span></div>
  <p class="compare-link">Gerðu verðsamanburð</p>
  <a href="#" class="btn btn-green" style="left:91px">VERÐVAKT</a>
</section>

<section class="card" style="left:764px">
  <div class="card-icon">
    <svg width="48" height="76" viewBox="0 0 48 76" fill="none" stroke="var(--green)" stroke-width="3" stroke-linejoin="round" stroke-linecap="round">
      <path d="M26 2L3 40h20l-6 34 28-42H26z"/>
    </svg>
  </div>
  <h2 class="card-title">Framtíðin Er Spennandi</h2>
  <p class="card-text narrow">Gerum raforkukerfið snallara saman. Kveldbrá notar gervigreind, gagnavísindi og sjálfvirkni til að lágmarka kostnað og stuðla að okrujöfnuði</p>
  <a href="#" class="btn btn-green" style="left:103px;top:322px">VITA MEIRA</a>
</section>

<footer class="site-footer">
  <div class="contact-icon" style="left:141px;top:38px">
    <svg width="24" height="20" viewBox="0 0 24 20" fill="none" stroke="var(--green)" stroke-width="1.4"><rect x="1" y="2" width="22" height="16"/><path d="M1 2l11 9 11-9"/></svg>
  </div>
  <div class="contact-text" style="left:195px;top:37px">kveldbra@kveldbra.is<br>555-0142</div>

  <div class="footer-brand"><span class="brand-dot"></span>Kveldbrá</div>

  <div class="contact-icon" style="left:796px;top:38px">
    <svg width="16" height="22" viewBox="0 0 16 22" fill="none" stroke="var(--green)" stroke-width="1.4"><path d="M8 21s7-8 7-13A7 7 0 0 0 1 8c0 5 7 13 7 13z"/><circle cx="8" cy="8" r="2.5"/></svg>
  </div>
  <div class="contact-text" style="left:852px;top:37px">HEIMILISFANG<br><span style="font-size:13px;line-height:25px">Dæmigötu 4 170 Sólvöllum</span></div>

  <div class="company-info">Kveldbrá Ehf<br>Kennitala: 510101-2390<span class="sep">•</span>Vskm Númer: 104422</div>
</footer>

<div class="copyright">Copyright © Kveldbrá 2021 Allur Réttur Áskilin</div>

</body>
</html>
```